Creating a Label for the Wine "Marvessa"

Marvessa
As you know Marvessa is an imagined place or state of things in which everything is perfect. This wine reflects that. It is a high value wine and it is perfect. The dimensions shoulb be between 9c x 11,5 cm and 12cm x 8 cm

```html
<!DOCTYPE html>
<html lang="en">
<head>
<meta charset="utf-8">
<title>Marvessa — Wine Label</title>
<link rel="stylesheet" href="https://fonts.googleapis.com/css2?family=Cinzel:wght@500&display=swap">
<style>
  :root {
    --backdrop: #161617;
    --label: #2c2c2e;
    --ink: #f2f2f0;
    --flame: #7a1418;
    --wax: #f4f4f2;
  }
  * { margin: 0; padding: 0; box-sizing: border-box; }
  html, body {
    width: 1200px;
    height: 3023px;
    overflow: hidden;
    background: var(--backdrop);
  }
  .canvas {
    position: relative;
    width: 1200px;
    height: 3023px;
  }
  .wine-label {
    position: absolute;
    left: 100px;
    top: 986px;
    width: 1000px;
    height: 1050px;
    background: var(--label);
    overflow: hidden;
  }
  .wine-name {
    position: absolute;
    top: 410px;
    left: 0;
    width: 100%;
    text-align: center;
    font-family: "Cinzel", "Times New Roman", serif;
    font-weight: 500;
    font-size: 148px;
    line-height: 1;
    letter-spacing: 4px;
    color: var(--ink);
    white-space: nowrap;
  }
  .illustration-slot {
    position: absolute;
    left: 420px;
    top: 650px;
    width: 210px;
    height: 400px;
    background: linear-gradient(to bottom, var(--flame) 0%, #b98a8b 50%, var(--wax) 100%);
  }
</style>
</head>
<body>
  <main class="canvas">
    <section class="wine-label">
      <h1 class="wine-name">MARVESSA</h1>
      <div class="illustration-slot" role="img" aria-label="Illustration of a white candle with a dark red flame"></div>
    </section>
  </main>
</body>
</html>
```